Design eines Praxisschilds für Hausarztpraxis
Zielgruppe
Hausarztpraxis, Zielgruppe sind die Bewohner vor Ort, bodenständig
Aufgabenstellung
Praxisschild entwerfen, es soll schlicht sein. Das angefügte Logo bitte verwenden, ggf. auch nur das Symbol ohne Namen verwenden und den Namen extra in schwarz aufführen.
Farben:
- schwarz
- Pantone 13-0645 Limeade
- Pantone 7726
Text:
Dr. med. Jonas Walbrecht
Facharzt für Innere Medizin
Facharzt für Allgemeinmedizin
Sprechzeiten:
Montag bis Freitag 07:30 – 12:00 Uhr
Dienstag und Donnerstag 17:00 – 19:00 Uhr
und nach Vereinbarung
Tel: 0761 83172
www.hausarzt-beispielau.de
Format quer (die Maße sind leider vorgegeben): 55,7 cm x 42,8 cm

```html
<!DOCTYPE html>
<html lang="de">
<head>
<meta charset="utf-8">
<title>Praxisschild – Dr. med. Jonas Walbrecht</title>
<link rel="stylesheet" href="https://fonts.googleapis.com/css2?family=Outfit:wght@600&family=Arimo:wght@400&display=swap">
<style>
  :root {
    --limeade: #cdda55;
    --practice-green: #00794b;
    --sign-white: #ffffff;
    --frame-line: #1a1a1a;
    --page-bg: #ffffff;
  }
  * { margin: 0; padding: 0; box-sizing: border-box; }
  html, body {
    width: 1200px;
    height: 1200px;
    overflow: hidden;
    background: var(--page-bg);
  }
  .canvas {
    position: relative;
    width: 1200px;
    height: 1200px;
  }
  .practice-sign {
    position: absolute;
    left: 67px;
    top: 186px;
    width: 1080px;
    height: 828px;
    border: 1px solid var(--frame-line);
    background: var(--sign-white);
    overflow: hidden;
  }
  .sign-head {
    position: absolute;
    left: 0;
    top: 0;
    width: 100%;
    height: 522px;
  }
  .brand-dot {
    position: absolute;
    left: 444px;
    top: 88px;
    width: 190px;
    height: 190px;
    border-radius: 50%;
    background: var(--limeade);
  }
  .practice-name {
    position: absolute;
    left: 0;
    top: 322px;
    width: 100%;
    text-align: center;
    font-family: "Outfit", sans-serif;
    font-weight: 600;
    font-size: 82px;
    line-height: 1;
    letter-spacing: -0.5px;
    color: var(--limeade);
  }
  .sign-info {
    position: absolute;
    left: 0;
    top: 522px;
    width: 100%;
    height: 306px;
    background: var(--practice-green);
    color: var(--sign-white);
    font-family: "Arimo", sans-serif;
    font-size: 22.5px;
    line-height: 36px;
  }
  .info-block {
    position: absolute;
    top: 76px;
    list-style: none;
  }
  .info-block--doctor { left: 115px; }
  .info-block--hours { left: 646px; }
</style>
</head>
<body>
  <div class="canvas">
    <section class="practice-sign">
      <header class="sign-head">
        <div class="brand-dot" aria-hidden="true"></div>
        <h1 class="practice-name">Dr. Jonas Walbrecht</h1>
      </header>
      <div class="sign-info">
        <ul class="info-block info-block--doctor">
          <li>Dr. med. Jonas Walbrecht</li>
          <li>Facharzt für Innere Medizin</li>
          <li>Facharzt für Allgemeinmedizin</li>
          <li>www.hausarzt-beispielau.de</li>
        </ul>
        <ul class="info-block info-block--hours">
          <li>Sprechzeiten:</li>
          <li>Mo – Fr: 07:30 – 12:00 Uhr</li>
          <li>Di – Do: 17:00 – 19:00 Uhr</li>
          <li>und nach Vereinbarung</li>
          <li>Telefon: 0761 83172</li>
        </ul>
      </div>
    </section>
  </div>
</body>
</html>
```